Ember Relaywork - Field Service Brochure

We are looking for a one page marketing brochure that includes our rate sheet. I've attached the working we on on the rate page, several photos and several versions of our logo.

```html
<!DOCTYPE html>
<html lang="en">
<head>
<meta charset="utf-8">
<title>Ember Relaywork – Field Service Rates</title>
<link href="https://fonts.googleapis.com/css2?family=Montserrat:wght@400;500;600;700&display=swap" rel="stylesheet">
<style>
  :root{
    --brand-blue:#47709a;
    --brand-blue-dark:#3c6288;
    --sky-top:#2f5fae;
    --sky-bottom:#7ea3cf;
    --ink:#2b2f36;
    --muted:#555b63;
    --rule:#b9c2cc;
    --paper:#ffffff;
    --paper-tint:#f3f5f8;
    --backdrop:#e4e4e4;
  }
  *{box-sizing:border-box;margin:0;padding:0}
  html,body{width:810px;height:1200px;overflow:hidden;background:var(--backdrop)}
  body{font-family:"Montserrat",Arial,sans-serif;color:var(--ink)}
  .brochure{position:relative;width:810px;height:1200px;background:linear-gradient(180deg,var(--paper) 40%,var(--paper-tint));overflow:hidden}
  .hero{position:absolute;left:0;top:0;width:810px;height:560px}
  .gallery{position:absolute;top:555px;left:0;width:810px;height:145px}
  .gallery .thumb{position:absolute;top:0;width:142px;height:142px;border-radius:50%;border:3px solid #fff;box-shadow:0 2px 6px rgba(0,0,0,.25)}
  .thumb.one{left:141px;background:radial-gradient(circle at 40% 40%,#8fb2dd,#3f6fb2 70%)}
  .thumb.two{left:334px;background:radial-gradient(circle at 50% 35%,#c9c3b8,#6d7a88 75%)}
  .thumb.three{left:527px;background:radial-gradient(circle at 50% 50%,#9dbbe0,#3a66a8 70%)}
  .intro{position:absolute;top:723px;left:50px;width:710px;text-align:center;font-size:11.4px;line-height:15.6px;color:var(--ink)}
  .intro .brand-name{color:var(--brand-blue);font-weight:600}
  .block{position:absolute}
  .block h2{font-size:17px;font-weight:700;color:var(--brand-blue);line-height:22px;white-space:nowrap}
  .block h2 .light{font-weight:400;color:var(--muted)}
  .block .sub{font-size:17px;font-weight:400;color:var(--muted);line-height:22px;white-space:nowrap}
  .heading-wrap{position:relative;padding-left:13px;padding-bottom:6px;border-bottom:1px solid var(--rule)}
  .heading-wrap::before{content:"";position:absolute;left:2px;top:6px;width:1px;height:26px;background:var(--muted);transform:rotate(-28deg);transform-origin:top}
  .heading-wrap.short{border-bottom:none;padding-bottom:0}
  .heading-wrap.short::before{height:14px;top:4px}
  ul.list{list-style:none;margin-top:10px}
  ul.list li{position:relative;padding-left:14px;font-size:10.4px;line-height:18.5px;color:var(--ink)}
  ul.list li::before{content:"";position:absolute;left:2px;top:7px;width:5px;height:5px;border-radius:50%;background:var(--brand-blue)}
  ul.list li b{font-weight:700}
  ul.loose li{line-height:14.5px;margin-bottom:7px}
  .standard{left:34px;top:812px;width:380px}
  .premium{left:34px;top:948px;width:350px}
  .expenses{left:412px;top:812px;width:390px}
  .minimum{left:412px;top:944px;width:300px}
  .cert-badge{position:absolute;left:737px;top:1068px;width:42px;height:42px;border-radius:50%;border:3px solid var(--brand-blue);background:#fff}
  .signature{position:absolute;left:36px;top:1100px;width:340px;height:90px}
  .signature .mark{position:absolute;left:22px;top:18px;width:50px;height:50px;border-radius:50%;background:var(--brand-blue)}
  .signature .name{position:absolute;left:84px;top:26px;font-size:18px;font-weight:700;color:var(--brand-blue);letter-spacing:.3px}
  .signature .parent{position:absolute;left:84px;top:52px;font-size:7.5px;font-weight:600;color:var(--brand-blue)}
  .footer-bar{position:absolute;left:0;top:0;width:810px;height:1200px;pointer-events:none}
  .contact{position:absolute;left:390px;top:1145px;width:410px;display:flex;justify-content:flex-end;gap:10px;align-items:center;font-size:11px;color:#fff;white-space:nowrap}
  .contact .item{display:flex;align-items:center;gap:4px}
  .contact .sep{opacity:.8}
  .contact svg{width:10px;height:10px;fill:#fff}
</style>
</head>
<body>
<main class="brochure">

  <svg class="hero" viewBox="0 0 810 560" aria-hidden="false">
    <defs>
      <linearGradient id="skyFill" x1="0" y1="0" x2="0" y2="1">
        <stop offset="0" stop-color="var(--sky-top)"/>
        <stop offset="0.6" stop-color="var(--sky-bottom)"/>
        <stop offset="1" stop-color="#a89b86"/>
      </linearGradient>
    </defs>
    <polygon role="img" aria-label="Photo: field technicians on an orange lift servicing high-voltage switchgear insulators at a substation under a blue sky"
      points="0,0 810,0 810,418 405,537 0,418" fill="url(#skyFill)"/>
    <polygon class="accent-band" points="0,422 236,490 0,545" fill="var(--brand-blue)"/>
    <polygon class="accent-band" points="810,422 574,490 810,545" fill="var(--brand-blue)"/>
  </svg>

  <section class="gallery">
    <div class="thumb one" role="img" aria-label="Photo: technician on a lift beside a steel switch structure"></div>
    <div class="thumb two" role="img" aria-label="Photo: field engineer in hard hat and safety vest at work"></div>
    <div class="thumb three" role="img" aria-label="Photo: crew on a lift inside an overhead switch frame"></div>
  </section>

  <p class="intro"><span class="brand-name">Ember Relaywork</span> Company offers an expertly trained Field Service program that can provide technical guidance and assistance for your initial installation, sustaining maintenance, and repair of equipment manufactured by Ember Relaywork. A 4-6 week reservation for assistance is recommended to ensure that we can fully accommodate your desired schedule. Expedited service may be available upon request.</p>

  <section class="block standard">
    <div class="heading-wrap">
      <h2>Standard Rates <span class="light">(on-site) up to 10 hours</span></h2>
      <div class="sub">+ travel and per diem expenses</div>
    </div>
    <ul class="list">
      <li><b>$250 x 1.00 =</b> Monday through Friday rate per hour ($2500 minimum)</li>
      <li><b>$250 x 1.50 =</b> Saturday rate per hour</li>
      <li><b>$250 X 2.00 =</b> Sunday rate per hour</li>
    </ul>
  </section>

  <section class="block premium">
    <div class="heading-wrap">
      <h2>Premium Rates <span class="light">(on-site) over 8 hours</span></h2>
      <div class="sub">+travel and per diem expenses</div>
    </div>
    <ul class="list">
      <li><b>$250 X 1.50 =</b> Over Time (9-12 hours) rate per hour</li>
      <li><b>$250 x 2.00 =</b> Double Time (Over 12 hours) rate per hour</li>
      <li><b>$250 X 2.50 =</b> Non-standard overnight hours</li>
    </ul>
  </section>

  <section class="block expenses">
    <div class="heading-wrap short"><h2>Expenses</h2></div>
    <ul class="list">
      <li><b>Airfare -</b> invoiced at actual cost + 25%</li>
      <li><b>Lodging -</b> invoiced at actual cost + 25%</li>
      <li><b>Meals and Incidentals –</b> invoiced at cost (not to exceed $100/day)</li>
      <li><b>Rental Vehicle and related costs –</b> Invoiced at cost +25%</li>
    </ul>
  </section>

  <section class="block minimum">
    <div class="heading-wrap short"><h2>Minimum Charge</h2></div>
    <ul class="list loose">
      <li>The minimum charge, excluding travel time and expenses shall be the equivalent of one 10 hour day</li>
      <li>Cancellation charge of 4 standard hours plus any non-cancellable airfare or lodging charges shall apply</li>
      <li>Employee Drug Screening</li>
      <li>Drug screening and/or background check costs (if required by customer) shall be invoiced at actual cost plus 30%.</li>
    </ul>
  </section>

  <div class="cert-badge" role="img" aria-label="Quality certification badge"></div>

  <svg class="footer-bar" viewBox="0 0 810 1200" aria-hidden="true">
    <polygon points="30,1100 330,1100 346,1117 30,1117" fill="#eef1f5"/>
    <polygon points="338,1130 810,1130 810,1183 372,1183" fill="var(--brand-blue)"/>
  </svg>

  <div class="signature">
    <div class="mark"></div>
    <div class="name">EMBER RELAYWORK</div>
    <div class="parent">A Northfield Grid Holdings Company</div>
  </div>

  <div class="contact">
    <span class="item"><svg viewBox="0 0 24 24"><path d="M6.6 10.8a15.1 15.1 0 0 0 6.6 6.6l2.2-2.2c.3-.3.7-.4 1-.2 1.1.4 2.3.6 3.6.6.6 0 1 .4 1 1V20c0 .6-.4 1-1 1A17 17 0 0 1 3 4c0-.6.4-1 1-1h3.5c.6 0 1 .4 1 1 0 1.3.2 2.5.6 3.6.1.3 0 .7-.2 1z"/></svg>800.555.0142</span>
    <span class="sep">|</span>
    <span class="item"><svg viewBox="0 0 24 24"><rect x="5" y="3" width="14" height="6"/><rect x="3" y="9" width="18" height="9" rx="2"/><rect x="7" y="14" width="10" height="7"/></svg>205.555.0187</span>
    <span class="sep">|</span>
    <span class="item"><svg viewBox="0 0 24 24"><circle cx="12" cy="12" r="10"/></svg>www.<b>emberrelaywork</b>.com</span>
  </div>

</main>
</body>
</html>
```